advertising board Hovarlunde BV

I have an advertisement spot in a small indoor football stadium, with the size of 1.00 x 22.00 meters. I want to show a design that stands out. My company works in Civil constructions and actually installs steel sheet piles and earth retaining walls in the most difficult to reach locations.

```html
<!DOCTYPE html>
<html lang="nl">
<head>
<meta charset="utf-8">
<title>Hovarlunde BV – advertising board</title>
<link href="https://fonts.googleapis.com/css2?family=Open+Sans:wght@400;600;700;800&display=swap" rel="stylesheet">
<style>
  :root{
    --page:#eeeeee;
    --brand-blue:#2aa9e0;
    --brand-blue-dark:#1b7fc4;
    --ink:#1d1d1f;
    --dark:#2b2b2d;
    --dark-2:#3a3a3c;
    --white:#ffffff;
    --photo-site-a:#6b6257;
    --photo-site-b:#a98a4a;
    --photo-water-a:#4f7a3e;
    --photo-water-b:#5f7f95;
  }
  *{box-sizing:border-box;margin:0;padding:0}
  html,body{width:1200px;height:609px;overflow:hidden;background:var(--page)}
  body{font-family:"Open Sans",Arial,sans-serif;position:relative}
  .board{
    position:absolute;left:20px;top:278px;width:1160px;height:53px;
    background:var(--dark);overflow:hidden;
  }
  .seg{position:absolute;top:0;height:100%}
  .brand{
    left:0;width:200px;background:var(--brand-blue);
    clip-path:polygon(0 0,100% 0,calc(100% - 8px) 100%,0 100%);
  }
  .brand-card{
    position:absolute;left:12px;top:0;width:178px;height:100%;background:var(--white);
    clip-path:polygon(8px 0,100% 0,calc(100% - 8px) 100%,0 100%);
    display:flex;flex-direction:column;justify-content:center;align-items:center;
  }
  .brand-name{font-weight:800;font-size:21px;line-height:1;color:var(--brand-blue-dark);letter-spacing:-.3px}
  .brand-tagline{font-size:4.6px;color:var(--ink);margin-top:3px;white-space:nowrap}
  .photo-site{
    left:186px;width:72px;
    background:linear-gradient(135deg,var(--photo-site-a),var(--photo-site-b) 70%,#5c5a55);
    clip-path:polygon(8px 0,100% 0,calc(100% - 8px) 100%,0 100%);
  }
  .services{
    left:250px;width:344px;background:linear-gradient(90deg,var(--dark-2),var(--dark));
    display:flex;align-items:center;justify-content:space-between;padding:0 22px 0 16px;
  }
  .service{display:flex;align-items:center;gap:5px;color:var(--white);font-weight:700;font-size:6.4px;line-height:1.15;text-transform:uppercase;white-space:nowrap}
  .service svg{width:15px;height:15px;flex:none}
  .photo-water{
    left:586px;width:96px;
    background:linear-gradient(160deg,var(--photo-water-a),var(--photo-water-b) 55%,var(--photo-water-a));
    clip-path:polygon(8px 0,100% 0,calc(100% - 8px) 100%,0 100%);
  }
  .contact{
    left:674px;width:486px;background:var(--brand-blue);color:var(--white);
    clip-path:polygon(8px 0,100% 0,100% 100%,0 100%);
    padding:5px 14px 0 24px;
  }
  .address{display:flex;align-items:center;gap:4px;font-weight:700;font-size:9.4px;white-space:nowrap}
  .address svg{width:7px;height:10px}
  .contact-main{display:flex;justify-content:space-between;align-items:center;margin-top:3px;white-space:nowrap}
  .phone{display:flex;align-items:center;gap:7px;font-weight:700;font-size:19px;letter-spacing:.3px}
  .phone svg{width:14px;height:14px}
  .web{font-weight:800;font-size:19px;letter-spacing:.2px}
</style>
</head>
<body>
  <div class="board">
    <div class="seg brand">
      <div class="brand-card">
        <span class="brand-name">Hovarlunde</span>
        <span class="brand-tagline">damwandconstructies - onderhoud - beschoeiingen - grondwerk</span>
      </div>
    </div>
    <div class="seg photo-site" role="img" aria-label="Photo of an excavator installing steel sheet piles on a building site"></div>
    <div class="seg services">
      <div class="service">
        <svg viewBox="0 0 16 16"><circle cx="8" cy="8" r="8" fill="var(--brand-blue)"/><path d="M4 8h6M8 5l3 3-3 3" stroke="#fff" stroke-width="1.6" fill="none"/></svg>
        <span>Damwand &amp;<br>constructies</span>
      </div>
      <div class="service">
        <svg viewBox="0 0 16 16"><circle cx="8" cy="8" r="8" fill="var(--brand-blue)"/><path d="M5 11l4-4M9 7a2 2 0 1 0 2-2" stroke="#fff" stroke-width="1.6" fill="none"/></svg>
        <span>Onderhoud &amp;<br>reparatie</span>
      </div>
      <div class="service">
        <svg viewBox="0 0 16 16"><circle cx="8" cy="8" r="8" fill="var(--brand-blue)"/><path d="M8 4v3M5 10V8h6v2" stroke="#fff" stroke-width="1.3" fill="none"/><rect x="6.5" y="3" width="3" height="2" fill="#fff"/><rect x="3.5" y="10" width="3" height="2.5" fill="#fff"/><rect x="9.5" y="10" width="3" height="2.5" fill="#fff"/></svg>
        <span>Grondwerk</span>
      </div>
      <div class="service">
        <svg viewBox="0 0 16 16"><circle cx="8" cy="8" r="8" fill="var(--brand-blue)"/><path d="M5 12l4-4" stroke="#fff" stroke-width="1.6"/><rect x="7.5" y="3.5" width="5" height="3" transform="rotate(45 10 5)" fill="#fff"/></svg>
        <span>Beschoeiingen</span>
      </div>
    </div>
    <div class="seg photo-water" role="img" aria-label="Aerial photo of a work pontoon along a canal bank with green grass"></div>
    <div class="seg contact">
      <div class="address">
        <svg viewBox="0 0 7 10"><circle cx="3.5" cy="3" r="2.6" fill="#fff"/><path d="M3.5 5v5" stroke="#fff" stroke-width="1.2"/></svg>
        <span>Hovarlunde B.V., Molenkade 7 9981XZ Oosterwaard</span>
      </div>
      <div class="contact-main">
        <div class="phone">
          <svg viewBox="0 0 24 24"><path fill="#fff" d="M6.6 10.8a15 15 0 0 0 6.6 6.6l2.2-2.2a1 1 0 0 1 1-.25 11.4 11.4 0 0 0 3.6.57 1 1 0 0 1 1 1V20a1 1 0 0 1-1 1A17 17 0 0 1 3 4a1 1 0 0 1 1-1h3.5a1 1 0 0 1 1 1c0 1.25.2 2.45.57 3.57a1 1 0 0 1-.25 1z"/></svg>
          <span>012 345 67 89</span>
        </div>
        <span class="web">www.hovarlunde.nl</span>
      </div>
    </div>
  </div>
</body>
</html>
```